Larkmoor Health- Core Values Graphic for Visual Appeal

I would like a poster that could take these written core values from our organization and create a graphic that we could use for our staff and employees. I would also like to incorporate our branding into this project. Thank you!

Target Market(s)

To helps patients and employees understand the core values of our organization

Industry/Entity Type

Healthcare

Requirements
Must have
• Match our branding
Nice to have
• Please use your creativity!
Should not have
• Overly complex/ busy

```html
<!DOCTYPE html>
<html lang="en">
<head>
<meta charset="UTF-8">
<title>Larkmoor Health – Our Core Values</title>
<link href="https://fonts.googleapis.com/css2?family=Montserrat:wght@400;500;700;800;900&family=Lato:wght@400&display=swap" rel="stylesheet">
<style>
  :root {
    --sky: #56c1de;
    --sky-light: #6fcbe4;
    --pattern-tone: #4fbadb;
    --brand-blue: #1577b8;
    --icon-dark: #2f86c8;
    --icon-light: #7fa3d8;
    --ink: #141414;
    --white: #ffffff;
    --line: #111111;
  }
  * { margin: 0; padding: 0; box-sizing: border-box; }
  html, body { width: 900px; height: 1200px; overflow: hidden; background: var(--sky); }
  .poster {
    position: relative;
    z-index: 0;
    width: 900px;
    height: 1200px;
    overflow: hidden;
    background: var(--sky);
    font-family: "Montserrat", sans-serif;
    color: var(--ink);
  }
  .bg-circle {
    position: absolute;
    left: -200px;
    top: 895px;
    width: 480px;
    height: 480px;
    border-radius: 50%;
    background: var(--sky-light);
    opacity: 0.55;
  }
  .corner-ring {
    position: absolute;
    left: 725px;
    top: -135px;
    width: 380px;
    height: 390px;
    border-radius: 50%;
    background: var(--white);
  }
  .corner-cut {
    position: absolute;
    left: 835px;
    top: -90px;
    width: 160px;
    height: 225px;
    border-radius: 50%;
    background: var(--sky);
  }
  .brand {
    position: absolute;
    left: 758px;
    top: 142px;
    display: flex;
    align-items: center;
    gap: 5px;
  }
  .brand-dot {
    width: 10px;
    height: 10px;
    border-radius: 50%;
    background: var(--brand-blue);
  }
  .brand-name {
    font-family: "Montserrat", sans-serif;
    font-weight: 700;
    font-size: 13px;
    color: var(--brand-blue);
    white-space: nowrap;
  }
  .title {
    position: absolute;
    left: 64px;
    top: 42px;
    font-weight: 800;
    font-size: 72px;
    letter-spacing: -0.5px;
    color: var(--white);
    line-height: 1;
    white-space: nowrap;
  }
  .title-rule {
    position: absolute;
    left: 66px;
    top: 163px;
    width: 183px;
    height: 12px;
    background: var(--brand-blue);
  }
  .intro {
    position: absolute;
    left: 288px;
    top: 122px;
    width: 388px;
    font-family: "Lato", sans-serif;
    font-size: 18.5px;
    line-height: 20.2px;
    color: var(--white);
  }
  .pattern-area {
    position: absolute;
    left: 681px;
    top: 415px;
    width: 178px;
    height: 115px;
    border-radius: 6px;
    background: var(--pattern-tone);
  }
  .treatment-photo {
    position: absolute;
    left: 560px;
    top: 830px;
    width: 340px;
    height: 370px;
    background:
      radial-gradient(ellipse at 70% 55%, rgba(228, 196, 176, 0.95) 0%, rgba(214, 180, 160, 0.7) 30%, rgba(200, 222, 232, 0.5) 60%, rgba(86, 193, 222, 0) 80%),
      linear-gradient(180deg, rgba(86, 193, 222, 0) 0%, rgba(226, 236, 242, 0.85) 70%, #eef3f6 100%);
  }
  .value {
    position: absolute;
    left: 65px;
    width: 535px;
    height: 181px;
    background: var(--white);
    border-radius: 13px;
  }
  .value::before {
    content: "";
    position: absolute;
    left: 88px;
    top: 66px;
    right: -15px;
    bottom: -14px;
    border-right: 3px solid var(--line);
    border-bottom: 3px solid var(--line);
    border-bottom-right-radius: 18px;
    z-index: -1;
  }
  .value-icon {
    position: absolute;
    left: -41px;
    top: 50px;
    width: 81px;
    height: 81px;
    border-radius: 5px;
    background: linear-gradient(90deg, var(--icon-dark) 0 41px, var(--icon-light) 41px 100%);
  }
  .value-name {
    position: absolute;
    left: 76px;
    top: 18px;
    font-weight: 900;
    font-size: 32px;
    letter-spacing: 1px;
    color: var(--brand-blue);
    line-height: 1.2;
  }
  .value-text {
    position: absolute;
    left: 75px;
    top: 64px;
    width: 432px;
    font-size: 12.6px;
    line-height: 15px;
    letter-spacing: 0.45px;
  }
  .value--family { top: 243px; }
  .value--excellence { top: 477px; }
  .value--excellence .value-text { top: 60px; }
  .value--integrity { top: 706px; }
  .value--service { top: 933px; }
  .value--service .value-text { top: 66px; }
</style>
</head>
<body>
<main class="poster">
  <div class="bg-circle"></div>
  <div class="treatment-photo" role="img" aria-label="Photo of a patient lying down receiving a gentle neck treatment from a practitioner"></div>

  <div class="corner-ring"></div>
  <div class="corner-cut"></div>
  <div class="brand">
    <span class="brand-dot"></span>
    <span class="brand-name">Larkmoor Health</span>
  </div>

  <h1 class="title">Our Core Values</h1>
  <div class="title-rule"></div>
  <p class="intro">These core values are the spirit of who we are as a healthcare team. They guide our actions, unite us in purpose, and ensure that we provide world-class care while fostering a positive and supportive atmosphere within our team:</p>

  <div class="pattern-area" role="img" aria-label="Decorative dot grid pattern"></div>

  <section class="value value--family">
    <div class="value-icon" role="img" aria-label="Icon of a group of three people"></div>
    <h2 class="value-name">FAMILY</h2>
    <p class="value-text">At the heart of our mission is the commitment to provide high-quality, affordable healthcare in a comforting and uplifting family-oriented environment. Just as our community is our extended family, every patient is a cherished member of our healthcare family. We treat each individual with the same care, compassion, and respect we would offer to our own loved ones.</p>
  </section>

  <section class="value value--excellence">
    <div class="value-icon" role="img" aria-label="Icon of people standing on a winners podium"></div>
    <h2 class="value-name">EXCELLENCE</h2>
    <p class="value-text">In line with our goal, we aspire not only to alleviate pain but also to inspire patients to become active participants in their well-being. We believe in empowering our patients through education and compassion. Our pursuit of excellence is unwavering, driven by our dedication to continuously improve our services at every level, ensuring that our community receives nothing less than exceptional care.</p>
  </section>

  <section class="value value--integrity">
    <div class="value-icon" role="img" aria-label="Icon of an umbrella sheltering a group of people"></div>
    <h2 class="value-name">INTEGRITY</h2>
    <p class="value-text">In our healthcare team, 'Integrity' is non-negotiable. Our purpose is deeply rooted in ethics, integrity, and professional standards. We operate with the utmost integrity in every aspect of our work, adhering to the highest ethical principles. We understand that trust is the foundation of healthcare, and we are committed to maintaining the trust our community places in us.</p>
  </section>

  <section class="value value--service">
    <div class="value-icon" role="img" aria-label="Icon of two hands supporting a person"></div>
    <h2 class="value-name">SERVICE</h2>
    <p class="value-text">Our vision is grounded in the belief that every person possesses the innate potential for true health. We aim to facilitate the body's natural healing response by providing the highest level of service. Our hope for each patient extends beyond healing; we aspire to help you fulfill your life's mission and purpose abundantly, supporting you in your journey to well-being.</p>
  </section>
</main>
</body>
</html>
```